Design Fresh and modern brochure about hypnosis

We need a clean and modern brochure designed for our hypnosis center. I have text, a logo, and a single image. I'd like all placed in a tri-fold brochure with design elements added and I'd like the result in a format which can be modified, like InDesign. The brochure should appear modern and clean, but also with a softer look to appear compassionate. The company values are professional, compassionate, and local. Local is the Pacific Northwest. Colors should match the logo, blue with elements of water. I'd like to see shades of blue with white.
Updates

Hello designers. Thank you all for your great brochure designs thus far. 

At this time I've narrowed down the top 2 designs and those designers have been contacted. 

So right now, any new designs would be in consideration for third place. I want to be fair to your time, so please consider if you're still interested in submitting a design for 3rd place or not. 

Thank you. 

Target Market(s)

Adults in western US who want to improve their lives. Primarily 30+ in age, english speaking, and working full or part time.

Industry/Entity Type

It Company

Colors
85cae6
0555a3
3276b5
86cfc6
32b7a4

Requirements
Must have
• The brochure must include the logo and image attached, and should fit in the tri-fold design, similar to the example brochure. It also needs to be in a format that can be easily modified over time, as I typically change text in the brochure. InDesign would be great.
Nice to have
• Additional design elements - like areas for a call-out to highlight features.

```html
<!DOCTYPE html>
<html lang="en">
<head>
<meta charset="utf-8">
<title>Hypnosis Brochure</title>
<link href="https://fonts.googleapis.com/css2?family=Arimo:wght@400;700&display=swap" rel="stylesheet">
<style>
  :root {
    --frame: #5b8c9c;
    --panel-edge: #6f9fb0;
    --panel-mid: #b6d6df;
    --panel-light: #d6eaef;
    --pill: #1592a2;
    --pill-border: #ffffff;
    --ink: #1b3752;
    --card: #a9d4e2;
    --card-edge: #d4ecf3;
    --photo-sky: #7fb2d6;
    --photo-sky-light: #cfe3f2;
    --white: #ffffff;
  }
  * { box-sizing: border-box; margin: 0; padding: 0; }
  html, body { width: 1200px; height: 885px; overflow: hidden; background: var(--frame); }
  body { font-family: "Arimo", Arial, sans-serif; color: var(--ink); }

  .brochure {
    position: relative;
    width: 1200px; height: 885px;
    background: var(--frame);
    padding: 18px;
  }
  .brochure__inner {
    position: absolute; inset: 18px;
    background: radial-gradient(ellipse 60% 65% at 50% 30%, var(--panel-light) 0%, var(--panel-mid) 45%, var(--panel-edge) 100%);
  }

  .section { position: absolute; }
  .section__title {
    height: 40px;
    border: 2px solid var(--pill-border);
    border-radius: 12px;
    background: var(--pill);
    color: var(--white);
    font-size: 18px;
    line-height: 36px;
    padding-left: 14px;
    margin-bottom: 14px;
  }
  .section p {
    font-size: 12.6px;
    line-height: 20.5px;
    text-align: justify;
    margin-bottom: 20px;
  }

  .col-left { left: 29px; width: 370px; }
  .col-mid { left: 412px; width: 364px; }
  .col-right { left: 803px; width: 374px; }

  .contact-card {
    position: absolute;
    left: 786px; top: 430px;
    width: 391px; height: 445px;
    background: radial-gradient(ellipse 80% 60% at 50% 100%, var(--card-edge) 0%, var(--card) 70%);
    border: 1px solid var(--card-edge);
    text-align: center;
    color: var(--white);
  }
  .contact-card__photo {
    position: absolute;
    left: 20px; top: 11px;
    width: 362px; height: 243px;
    background: linear-gradient(180deg, var(--photo-sky) 0%, var(--photo-sky-light) 100%);
  }
  .contact-card__tagline {
    position: absolute; left: 0; right: 0; top: 270px;
    font-size: 20px; letter-spacing: 0.5px;
  }
  .contact-card__cta {
    position: absolute; left: 0; right: 0; top: 328px;
    font-size: 21px; font-weight: 700;
  }
  .contact-card__phone {
    position: absolute; left: 0; right: 0; top: 356px;
    font-size: 35px; font-weight: 700;
  }
</style>
</head>
<body>
<div class="brochure">
  <div class="brochure__inner"></div>

  <section class="section col-left" style="top:32px">
    <h2 class="section__title">What is Hypnosis?</h2>
    <p>Hypnosis is a state of focused consciousness. Your hypnotherapist will assist you in learning how to achieve this state by guiding you into it.</p>
    <p>Once this has been achieved, you will then receive what are called hypnotic suggestions. These suggestions will enable you to use the power of hypnosis in your life and make the changes you desire.</p>
    <p>Hypnosis is a tool that can help you just, like it has helped millions of other people to take back control of their lives. Hypnosis can help you change old habits and to provide you with motivation to do the things that you may have been putting off.</p>
    <p>Hypnosis has been sanctioned and used by the medical community since 1958 to help patients overcome chronic pain, create anesthesia, and heal psychogenic illnesses.</p>
    <p>Hypnosis and self-hypnosis have been shown to be effective in reducing stress and stress-related illnesses.</p>
    <p>Hypnosis has also been shown to help mothers give birth to their children with little or no pain.</p>
  </section>

  <section class="section col-left" style="top:607px">
    <h2 class="section__title">Is Hypnosis safe?</h2>
    <p>Hypnosis is safe. It is very similar to experiencing a daydream. Usually you will feel relaxed when doing hypnosis. Hypnosis in and of itself is a very pleasant experience. It is a time to let go of the other thoughts of the day and focus on the issues you came in to work on. Scientist, medical professionals, psychologists and hypnotherapists have been using hypnosis for over 200 years and no one has ever been hurt by simply going into hypnosis.</p>
  </section>

  <section class="section col-mid" style="top:32px">
    <h2 class="section__title">What is Hypnotherapy?</h2>
    <p>Hypnotherapy is the applied use of hypnosis. Therapy can be defined as anything that is done to move someone toward health and wholeness. Thus, hypnotherapy is the use of hypnosis to help you move toward health and wholeness.</p>
    <p>Hypnotherapy is also used to help you reach goals when nothing else has helped. See the back panel of this brochure to see a list of uses for hypnotherapy.</p>
    <p>Self-hypnosis may also be part of a good hypnotherapy program. Ask your hypnotherapist if using self-hypnosis is recommended to help you reach your goals.</p>
  </section>

  <section class="section col-mid" style="top:375px">
    <h2 class="section__title">Can I be Hypnotized?</h2>
    <p>Of course you can! You already have been. It's easy to go into hypnosis and it is a normal state of mind that everyone has already experienced.</p>
    <p>In fact, hypnosis is such a normal state of mind, most people usually don't even realize that they are hypnotized.</p>
    <p>Normal, everyday hypnosis occurs when you are driving down the road and lose track of time, or, when you are focusing on a book or television program and you don't even notice something that is going on around you</p>
    <p>When you come in for hypnosis, all you need to do is to be able to follow the instructions of the hypnotherapist and you can put the power of hypnosis to work for you.</p>
    <p>Anyone of with the willingness and ability to follow instructions can experience hypnosis and use it to improve his or her life. This includes children and teenagers.</p>
  </section>

  <section class="section col-right" style="top:32px">
    <h2 class="section__title">Who will Hypnotize me?</h2>
    <p>Your hypnotist or hypnotherapist is a highly qualified professional. He or she is certified and registered with the Northwest Council of Hypnotists.</p>
    <p>Your hypnotherapist is bound by professional ethics and the laws of the state in which it is practiced.</p>
    <p>In addition, your hypnotherapist has achieved extra certification in the advanced hypnotherapy system called CALM-STEP. Rest assured that he or she will treat you with respect, and that your visits are completely confidential.</p>
    <p>We suggest that you call and speak to us directly so that you can learn more about hypnosis and hypnotherapy. This will allow you to become more familiar with the programs offered and allow us to answer your questions.</p>
  </section>

  <aside class="contact-card">
    <div class="contact-card__photo" role="img" aria-label="Photo of a relaxed man with closed eyes against a soft blue sky with light clouds"></div>
    <div class="contact-card__tagline">COME FIND PEACE AND HAPPINESS</div>
    <div class="contact-card__cta">CALL US TODAY</div>
    <div class="contact-card__phone">(360) 555-0147</div>
  </aside>
</div>
</body>
</html>
```